Modify mobile web Photoshop design to make them look great

We need to choose and refine the stock image to look great on 5 mobile web pages: 1) Hourglass image on home screen, 2) Sofa image on registration screen, 3) Loveseat image on login screen, 4) Lamp for reminder screen, and 5) Bed for ratings / score screen. Sample photos denote what customer wants, but they are just downloaded from Vantry, and is not purchased stock photos. Designers need to show that the updated photos used are properly purchased from stock photo source. Photoshop files for all 5 mobile web pages are provided. Artists are requested to edit and submit the 5 photoshop files and make them look as good as possible with the constraints above. No change is needed on the layout or anything beside the 5 stock images, but subtle refinements are OK if you believe it would improve the overall design without affecting the art direction.

Target Market(s)

Travel, Lifestyle

Industry/Entity Type

Hospitality

Font styles to use
Sans Serif

Requirements
Must have
• Stock photos must be properly licensed, artists must put updated stock photos back into supplied photoshop source files, updated look and feel should have the same general art direction, images must be hourglass, sofa, loveseat, lamp and bed
Nice to have
• Minor and very subtle touchup of other elements without affecting any design work of the layout such as color scheme
Should not have
• Should not affect art direction, identity and color of all design and layout elements, should not use stock image other than the types specified (hourglass, sofa, loveseat, lamp and bed), should not use images not licensed from stock photo sites

```html
<!DOCTYPE html>
<html lang="en">
<head>
<meta charset="utf-8">
<title>restly.co – Login</title>
<link href="https://fonts.googleapis.com/css2?family=Open+Sans:wght@400;600;700;800&display=swap" rel="stylesheet">
<style>
  :root {
    --ink: #111111;
    --text: #555555;
    --white: #ffffff;
    --lilac: #b07fd8;
    --lilac-line: #a678d8;
    --teal: #079792;
    --teal-soft: #5fb5b0;
    --plum: #a0127a;
    --peach: #f2b283;
    --wall-top: #cbc9c8;
    --wall-mid: #dcdad9;
    --sofa-tone: #d9a0a3;
    --floor: #f4f4f4;
  }
  * { box-sizing: border-box; margin: 0; padding: 0; }
  html, body { width: 676px; height: 1200px; overflow: hidden; }
  body { font-family: "Open Sans", Arial, sans-serif; background: var(--white); }
  .screen { position: relative; width: 676px; height: 1200px; overflow: hidden; }
  .backdrop {
    position: absolute; inset: 0;
    background: linear-gradient(180deg,
      var(--wall-top) 0%,
      var(--wall-mid) 45%,
      #e6e4e3 64%,
      var(--sofa-tone) 67%,
      var(--sofa-tone) 81%,
      var(--floor) 84%,
      var(--white) 100%);
  }
  .top-bar { position: absolute; top: 0; left: 0; width: 100%; height: 96px; }
  .back-button { position: absolute; left: 36px; top: 28px; }
  .brand {
    position: absolute; left: 0; right: 0; top: 14px; text-align: center;
    font-weight: 800; font-size: 52px; letter-spacing: -2px; color: var(--ink);
  }
  .menu-button { position: absolute; left: 600px; top: 37px; }
  .login-card {
    position: absolute; left: 47px; top: 377px; width: 581px; height: 315px;
    border: 1.5px solid rgba(255,255,255,0.9); border-radius: 10px;
    background: rgba(255,255,255,0.22);
  }
  .field {
    position: absolute; left: 34px; width: 507px; height: 57px;
    background: var(--white); border-radius: 10px;
    display: flex; align-items: center;
  }
  .field--user { top: 34px; border-bottom: 2px solid var(--lilac-line); }
  .field--pass { top: 109px; border-bottom: 2px solid var(--teal); }
  .field-icon { width: 56px; display: flex; justify-content: center; }
  .field-divider { width: 1px; height: 32px; background: #777; }
  .field-label { padding-left: 9px; font-size: 18px; color: var(--text); }
  .link-row {
    position: absolute; left: 34px; width: 507px; top: 178px;
    display: flex; justify-content: space-between; font-size: 18px;
  }
  .link-register { color: var(--teal-soft); font-weight: 600; }
  .link-forgot { color: var(--plum); }
  .login-button {
    position: absolute; left: 35px; top: 221px; width: 506px; height: 48px;
    background: var(--peach); border-radius: 4px;
    color: var(--white); font-size: 20px; display: flex; align-items: center; justify-content: center;
  }
  .pager { position: absolute; top: 1091px; left: 267px; display: flex; gap: 13px; }
  .dot { width: 20px; height: 20px; border-radius: 50%; }
</style>
</head>
<body>
<div class="screen">
  <div class="backdrop" role="img" aria-label="Photo of a red sofa with white cushions against a grey concrete wall"></div>

  <header class="top-bar">
    <svg class="back-button" width="24" height="34" viewBox="0 0 24 34" aria-label="Back">
      <polyline points="20,3 6,17 20,31" fill="none" stroke="#111" stroke-width="4"/>
    </svg>
    <div class="brand">restly.co</div>
    <svg class="menu-button" width="34" height="18" viewBox="0 0 34 18" aria-label="Menu">
      <g stroke="#111" stroke-width="2"><line x1="0" y1="1" x2="34" y2="1"/><line x1="0" y1="8" x2="34" y2="8"/><line x1="0" y1="15" x2="34" y2="15"/></g>
    </svg>
  </header>

  <section class="login-card">
    <div class="field field--user">
      <div class="field-icon">
        <svg width="24" height="28" viewBox="0 0 24 28"><g fill="none" stroke="var(--lilac)" stroke-width="1.6"><circle cx="12" cy="8" r="6"/><path d="M1 27c0-6 5-10 11-10s11 4 11 10z"/></g></svg>
      </div>
      <div class="field-divider"></div>
      <span class="field-label">User Name</span>
    </div>
    <div class="field field--pass">
      <div class="field-icon">
        <svg width="24" height="28" viewBox="0 0 24 28"><g fill="none" stroke="var(--teal)" stroke-width="1.6"><path d="M6 12V8a6 6 0 0 1 12 0v4"/><rect x="2" y="12" width="20" height="14" rx="2"/></g><text x="12" y="23" font-size="8" text-anchor="middle" fill="var(--teal)" font-family="Open Sans, sans-serif">0</text></svg>
      </div>
      <div class="field-divider"></div>
      <span class="field-label">Password</span>
    </div>
    <div class="link-row">
      <span class="link-register">Register now</span>
      <span class="link-forgot">Forgot Password?</span>
    </div>
    <div class="login-button">LOGIN</div>
  </section>

  <nav class="pager" aria-label="Pages">
    <span class="dot" style="background:var(--lilac)"></span>
    <span class="dot" style="background:var(--teal)"></span>
    <span class="dot" style="background:var(--plum)"></span>
    <span class="dot" style="background:var(--peach)"></span>
    <span class="dot" style="background:var(--teal)"></span>
  </nav>
</div>
</body>
</html>
```